Creative Web design for Tattoo Artist

I am a tattoo artist with a private tattoo/art studio in Spring, TX. I need to design a website for my studio, to include the following "pages" :
-home/about
-FAQ
-Gallery
-Inquiries
-shop
We would like to see designs that are more dark or "moody", and like the colors black/gold.
I'd like my website to reflect my studio, an award winning private, upscale custom only tattoo studio.

I've attached some examples of styles we liked.

Target Market(s)

adults ages 18-50, interested in tattoos, or fine art

Industry/Entity Type

Tattoos/Fine Art/Arts

Coding

Coded - Design and coding required

Number of Pages Required

5+ page

Colors

Designer to choose colors to be used in the design.

Requirements
Must have
• gallery section, and e-commerce page set up so I can begin selling merchandise, I'd like the fonts to flow with my logo design

```html
<!DOCTYPE html>
<html lang="en">
<head>
<meta charset="utf-8">
<title>Ravenmark Studio – Shop</title>
<link rel="stylesheet" href="https://fonts.googleapis.com/css2?family=Playfair+Display:wght@400;500&family=Mulish:wght@400;500&display=swap">
<style>
  :root {
    --ink: #111111;
    --header: #121212;
    --gold: #f6d390;
    --white: #ffffff;
    --text: #222222;
    --muted: #555555;
    --rule: #d6d6d6;
    --badge: #2f46d6;
    --tile: #e6e9ed;
  }
  * { margin: 0; padding: 0; box-sizing: border-box; }
  html, body { width: 1048px; height: 1200px; overflow: hidden; background: var(--white); }
  body { position: relative; font-family: "Playfair Display", serif; color: var(--text); }

  .site-header { position: absolute; left: 0; top: 0; width: 1048px; height: 90px; background: var(--header); }
  .brand { position: absolute; left: 110px; top: 30px; width: 80px; text-align: center; color: var(--white); font-size: 13px; line-height: 15px; font-family: "Playfair Display", serif; letter-spacing: 1px; }
  .main-nav { position: absolute; top: 38px; left: 0; width: 1048px; }
  .main-nav a { position: absolute; color: var(--gold); text-decoration: none; font-size: 12px; font-weight: 500; white-space: nowrap; }
  .main-nav a.current { color: var(--white); }
  .social { position: absolute; top: 25px; left: 944px; display: flex; gap: 5px; }
  .social span { width: 14px; height: 14px; border-radius: 50%; background: var(--white); display: block; }
  .cart { position: absolute; left: 1010px; top: 34px; }

  .hero { position: absolute; left: 0; top: 90px; width: 1048px; height: 321px;
    background: radial-gradient(ellipse at 70% 50%, #6b6b6b 0%, #3d3d3d 45%, #1f1f1f 100%); }
  .hero-title { position: absolute; left: 0; width: 1048px; top: 70px; text-align: center; color: var(--gold); font-size: 64px; font-weight: 400; letter-spacing: 28px; text-indent: 28px; line-height: 76px; }
  .hero-tagline { position: absolute; left: 0; width: 1048px; top: 150px; text-align: center; color: var(--gold); font-size: 25px; line-height: 34px; font-weight: 400; }

  .filters { position: absolute; left: 51px; top: 448px; width: 129px; }
  .filters h2 { font-size: 17px; font-weight: 400; color: var(--ink); height: 34px; border-bottom: 1px solid var(--rule); }
  .filter-row { display: flex; justify-content: space-between; align-items: center; font-size: 11px; color: var(--ink); height: 44px; border-bottom: 1px solid var(--rule); }
  .filter-price { border-bottom: 1px solid var(--rule); padding: 14px 0 10px; }
  .filter-price .head { display: flex; justify-content: space-between; font-size: 11px; color: var(--ink); }
  .slider { position: relative; height: 12px; margin: 10px 0 4px; }
  .slider::before { content: ""; position: absolute; left: 5px; right: 5px; top: 5px; height: 1px; background: #444; }
  .slider i { position: absolute; top: 0; width: 12px; height: 12px; border-radius: 50%; background: #444; }
  .range { display: flex; justify-content: space-between; font-size: 8.5px; color: var(--muted); padding: 0 2px; }

  .product { position: absolute; width: 195px; }
  .product .photo { width: 195px; height: 195px; position: relative; }
  .badge { position: absolute; left: 0; top: 0; background: var(--badge); color: var(--white); font-family: "Mulish", sans-serif; font-size: 8.5px; padding: 3px 7px; }
  .product h3 { font-size: 11px; font-weight: 400; color: var(--ink); margin-top: 10px; }
  .price { font-family: "Mulish", sans-serif; font-size: 8px; color: var(--muted); margin-top: 3px; }
</style>
</head>
<body>
  <header class="site-header">
    <div class="brand">Ravenmark<br>Studio</div>
    <nav class="main-nav">
      <a style="left:292px">About Us</a>
      <a style="left:402px">Gallery</a>
      <a style="left:501px">Inquiries</a>
      <a style="left:618px">FAQ</a>
      <a class="current" style="left:720px">Shop</a>
    </nav>
    <div class="social" aria-label="Social links"><span></span><span></span><span></span></div>
    <svg class="cart" width="14" height="19" viewBox="0 0 14 19" aria-label="Cart, 0 items">
      <path d="M4 6 V4 a3 3 0 0 1 6 0 V6" fill="none" stroke="#3852e6" stroke-width="1.2"/>
      <rect x="0.5" y="6" width="13" height="12.5" fill="#3852e6"/>
      <text x="7" y="15.5" text-anchor="middle" font-family="Mulish, sans-serif" font-size="6" fill="#fff">0</text>
    </svg>
  </header>

  <section class="hero" role="img" aria-label="Black and white photo of a tattoo artist in a hat working on a client's arm in the studio">
    <h1 class="hero-title">SHOP</h1>
    <p class="hero-tagline">Making your skin canvas beautiful, one<br>tattoo at a time</p>
  </section>

  <aside class="filters">
    <h2>Filtrar por</h2>
    <div class="filter-price">
      <div class="head"><span>Precio</span><span>–</span></div>
      <div class="slider"><i style="left:0"></i><i style="right:0"></i></div>
      <div class="range"><span>S/.7.50</span><span>S/.130.00</span></div>
    </div>
    <div class="filter-row"><span>Color</span><span>+</span></div>
    <div class="filter-row"><span>Size</span><span>+</span></div>
  </aside>

  <main class="product-grid">
    <article class="product" style="left:193px;top:437px">
      <div class="photo" role="img" aria-label="Dried flowers in a cream vase" style="background:linear-gradient(180deg,#cdc6bf,#d8d2cb 70%,#c9c3bb)"></div>
      <h3>I'm a product</h3><p class="price">S/.85.00</p>
    </article>
    <article class="product" style="left:400px;top:437px">
      <div class="photo" role="img" aria-label="White canvas tote bag" style="background:radial-gradient(circle at 50% 50%,#f4f5f6 0%,#e6e9ed 55%)"></div>
      <h3>I'm a product</h3><p class="price">S/.20.00</p>
    </article>
    <article class="product" style="left:607px;top:437px">
      <div class="photo" role="img" aria-label="Dropper bottle of serum" style="background:radial-gradient(circle at 50% 52%,#f0d7bf 0%,#e6e9ed 30%)"><span class="badge">Best Seller</span></div>
      <h3>I'm a product</h3><p class="price">S/.10.00</p>
    </article>
    <article class="product" style="left:815px;top:437px">
      <div class="photo" role="img" aria-label="Knit turtleneck sweater" style="background:radial-gradient(circle at 50% 50%,#c9c3ba 0%,#e6e9ed 45%)"></div>
      <h3>I'm a product</h3><p class="price">S/.25.00</p>
    </article>

    <article class="product" style="left:193px;top:682px">
      <div class="photo" role="img" aria-label="Black round eyeglasses" style="background:radial-gradient(ellipse at 50% 50%,#c9ccd0 0%,#e6e9ed 40%)"><span class="badge">New</span></div>
      <h3>I'm a product</h3><p class="price">S/.7.50</p>
    </article>
    <article class="product" style="left:400px;top:682px">
      <div class="photo" role="img" aria-label="Molded wooden lounge chair" style="background:radial-gradient(circle at 50% 48%,#d8a27a 0%,#e6e9ed 38%)"></div>
      <h3>I'm a product</h3><p class="price">S/.15.00</p>
    </article>
    <article class="product" style="left:607px;top:682px">
      <div class="photo" role="img" aria-label="Amber pump bottles on stone blocks" style="background:linear-gradient(180deg,#cdb6a3,#d4c2b2 60%,#c8b8a8)"></div>
      <h3>I'm a product</h3><p class="price">S/.85.00</p>
    </article>
    <article class="product" style="left:815px;top:682px">
      <div class="photo" role="img" aria-label="Black baseball cap" style="background:radial-gradient(circle at 55% 45%,#9a9ca0 0%,#e6e9ed 38%)"></div>
      <h3>I'm a product</h3><p class="price">S/.40.00</p>
    </article>

    <article class="product" style="left:193px;top:927px">
      <div class="photo" role="img" aria-label="Aluminium water bottle on a stone" style="background:linear-gradient(180deg,#d3c7b8,#d9cfc2 70%,#cbbfb0)"></div>
      <h3>I'm a product</h3><p class="price">S/.30.00</p>
    </article>
    <article class="product" style="left:400px;top:927px">
      <div class="photo" role="img" aria-label="White round soap bar" style="background:radial-gradient(circle at 45% 50%,#f7f7f7 0%,#e6e9ed 35%)"></div>
      <h3>I'm a product</h3><p class="price">S/.12.00</p>
    </article>
    <article class="product" style="left:607px;top:927px">
      <div class="photo" role="img" aria-label="Silver hoop earrings" style="background:radial-gradient(circle at 50% 50%,#d2d5d9 0%,#e6e9ed 35%)"><span class="badge">Sale</span></div>
      <h3>I'm a product</h3><p class="price">S/.18.00</p>
    </article>
    <article class="product" style="left:815px;top:927px">
      <div class="photo" role="img" aria-label="Model wearing a plain white t-shirt" style="background:linear-gradient(90deg,#b3ab98,#d8d6d0 50%,#b8b09e)"></div>
      <h3>I'm a product</h3><p class="price">S/.22.00</p>
    </article>
  </main>
</body>
</html>
```